5 CD Designs for 5 albums soon on tunewell and birch lantern

I'm looking for something fairly unique, i make music shameless plug: www.loopharbor.net/mirelynx and i'm looking for 5 EP covers. 4 of my EP's are allready listed called:

Glass & Linger
Salt & Fern
Cedar & Drift

and i'm working on a new one in the next month.

I'm looking for a unique design style that matches the music but also something that carries that same style across the 5 designs.

Now i know exposure doesn't pay the bills but i promise to give credit as much as i can, i'm also looking for someone who could keep providing artwork for the albums of the future

Font styles to use
Decorative
Script

Colors
ffffff
85cae6
0692cd

Requirements
Must have
• 5 unique designs
Nice to have
• a nominalistic representation of the music

```html
<!DOCTYPE html>
<html lang="en">
<head>
<meta charset="utf-8">
<title>EP Cover Series — mirelynx</title>
<link rel="stylesheet" href="https://fonts.googleapis.com/css2?family=Josefin+Sans:wght@300;400&display=swap">
<style>
  :root {
    --navy-band: #0d2a4d;
    --cover-bg: #0c2a4b;
    --page: #ffffff;
    --bar: #1d5674;
    --bar-soft: #174766;
    --stream: #0f5fd0;
    --stream-glow: #1b74e8;
    --text: #ffffff;
  }
  * { margin: 0; padding: 0; box-sizing: border-box; }
  html, body { width: 1200px; height: 1000px; overflow: hidden; background: var(--page); }
  .board { position: relative; width: 1200px; height: 1000px; background: var(--page); }
  .band { position: absolute; left: 0; width: 1200px; background: var(--navy-band); }
  .band--top { top: 0; height: 103px; }
  .band--bottom { top: 903px; height: 97px; }

  .cover {
    position: absolute; width: 339px; height: 339px;
    background: var(--cover-bg); overflow: hidden;
  }
  .cover--1 { left: 44px; top: 134px; }
  .cover--2 { left: 426px; top: 134px; }
  .cover--3 { left: 808px; top: 134px; }
  .cover--4 { left: 247px; top: 524px; }
  .cover--5 { left: 629px; top: 524px; }

  .cover__stream {
    position: absolute; left: 0; width: 100%; height: 110px;
    background:
      linear-gradient(180deg, rgba(15,95,208,0) 0%, rgba(15,95,208,0.28) 40%, rgba(27,116,232,0.75) 52%, rgba(15,95,208,0.25) 62%, rgba(15,95,208,0) 100%);
  }
  .cover__bars { position: absolute; left: 0; top: 0; width: 339px; height: 339px; }

  .cover__title {
    position: absolute; right: 22px; top: 40px;
    font-family: "Josefin Sans", sans-serif; font-weight: 300;
    font-size: 31px; letter-spacing: 1px; color: var(--text);
    white-space: nowrap; line-height: 1;
  }
  .cover__title .title__second {
    display: inline-block; margin-left: 3px; padding-left: 5px;
    border-left: 1px solid var(--text); transform: translateY(7px);
  }
  .cover__artist {
    position: absolute; left: 22px; bottom: 20px;
    display: flex; align-items: center; gap: 6px;
    font-family: "Josefin Sans", sans-serif; font-weight: 400;
    font-size: 15px; letter-spacing: 1px; color: var(--text);
  }
  .cover__artist::before {
    content: ""; width: 10px; height: 10px; border-radius: 50%; background: var(--text);
  }
</style>
</head>
<body>
<main class="board">
  <div class="band band--top"></div>

  <svg width="0" height="0" style="position:absolute" aria-hidden="true">
    <defs>
      <pattern id="meter-segment" width="31" height="12.8" patternUnits="userSpaceOnUse" x="2" y="3">
        <rect width="27" height="9" fill="var(--bar)" fill-opacity="0.8"/>
      </pattern>
    </defs>
  </svg>

  <section class="cover cover--1">
    <div class="cover__stream" style="top:130px" role="img" aria-label="Flowing blue light-stream illustration"></div>
    <svg class="cover__bars" viewBox="0 0 339 339" aria-hidden="true">
      <g fill="url(#meter-segment)">
        <rect x="2" y="100" width="27" height="239"/><rect x="33" y="190" width="27" height="149"/>
        <rect x="64" y="140" width="27" height="199"/><rect x="95" y="165" width="27" height="174"/>
        <rect x="126" y="205" width="27" height="134"/><rect x="157" y="240" width="27" height="99"/>
        <rect x="188" y="115" width="27" height="224"/><rect x="219" y="140" width="27" height="199"/>
        <rect x="250" y="128" width="27" height="211"/><rect x="281" y="165" width="27" height="174"/>
        <rect x="312" y="190" width="27" height="149"/>
      </g>
    </svg>
    <h2 class="cover__title">GLASS<span class="title__second">LINGER</span></h2>
    <p class="cover__artist">mirelynx</p>
  </section>

  <section class="cover cover--2">
    <div class="cover__stream" style="top:130px" role="img" aria-label="Flowing blue light-stream illustration"></div>
    <svg class="cover__bars" viewBox="0 0 339 339" aria-hidden="true">
      <g fill="url(#meter-segment)">
        <rect x="2" y="230" width="27" height="109"/><rect x="33" y="205" width="27" height="134"/>
        <rect x="64" y="255" width="27" height="84"/><rect x="95" y="180" width="27" height="159"/>
        <rect x="126" y="218" width="27" height="121"/><rect x="157" y="243" width="27" height="96"/>
        <rect x="188" y="205" width="27" height="134"/><rect x="219" y="255" width="27" height="84"/>
        <rect x="250" y="218" width="27" height="121"/><rect x="281" y="205" width="27" height="134"/>
        <rect x="312" y="230" width="27" height="109"/>
      </g>
    </svg>
    <h2 class="cover__title">SALT<span class="title__second">FERN</span></h2>
    <p class="cover__artist">mirelynx</p>
  </section>

  <section class="cover cover--3">
    <div class="cover__stream" style="top:135px" role="img" aria-label="Flowing blue light-stream illustration"></div>
    <svg class="cover__bars" viewBox="0 0 339 339" aria-hidden="true">
      <g fill="url(#meter-segment)">
        <rect x="2" y="165" width="27" height="174"/><rect x="33" y="100" width="27" height="239"/>
        <rect x="64" y="140" width="27" height="199"/><rect x="95" y="115" width="27" height="224"/>
        <rect x="126" y="165" width="27" height="174"/><rect x="157" y="100" width="27" height="239"/>
        <rect x="188" y="140" width="27" height="199"/><rect x="219" y="115" width="27" height="224"/>
        <rect x="250" y="140" width="27" height="199"/><rect x="281" y="100" width="27" height="239"/>
        <rect x="312" y="165" width="27" height="174"/>
      </g>
    </svg>
    <h2 class="cover__title">CEDAR<span class="title__second">DRIFT</span></h2>
    <p class="cover__artist">mirelynx</p>
  </section>

  <section class="cover cover--4">
    <div class="cover__stream" style="top:135px" role="img" aria-label="Flowing blue light-stream illustration"></div>
    <svg class="cover__bars" viewBox="0 0 339 339" aria-hidden="true">
      <g fill="url(#meter-segment)">
        <rect x="2" y="255" width="27" height="84"/><rect x="33" y="205" width="27" height="134"/>
        <rect x="64" y="243" width="27" height="96"/><rect x="95" y="192" width="27" height="147"/>
        <rect x="126" y="218" width="27" height="121"/><rect x="157" y="305" width="27" height="34"/>
        <rect x="188" y="243" width="27" height="96"/><rect x="219" y="218" width="27" height="121"/>
        <rect x="250" y="292" width="27" height="47"/><rect x="281" y="205" width="27" height="134"/>
        <rect x="312" y="255" width="27" height="84"/>
      </g>
    </svg>
    <h2 class="cover__title">GLASS<span class="title__second">LINGER</span></h2>
    <p class="cover__artist">mirelynx</p>
  </section>

  <section class="cover cover--5">
    <div class="cover__stream" style="top:140px" role="img" aria-label="Flowing blue light-stream illustration"></div>
    <svg class="cover__bars" viewBox="0 0 339 339" aria-hidden="true">
      <g fill="url(#meter-segment)">
        <rect x="2" y="140" width="27" height="199"/><rect x="33" y="165" width="27" height="174"/>
        <rect x="64" y="115" width="27" height="224"/><rect x="95" y="153" width="27" height="186"/>
        <rect x="126" y="140" width="27" height="199"/><rect x="157" y="178" width="27" height="161"/>
        <rect x="188" y="128" width="27" height="211"/><rect x="219" y="153" width="27" height="186"/>
        <rect x="250" y="102" width="27" height="237"/><rect x="281" y="153" width="27" height="186"/>
        <rect x="312" y="140" width="27" height="199"/>
      </g>
    </svg>
    <h2 class="cover__title">SALT<span class="title__second">FERN</span></h2>
    <p class="cover__artist">mirelynx</p>
  </section>

  <div class="band band--bottom"></div>
</main>
</body>
</html>
```